Flyer für Führungskräfte-Workshops und Coaching
Wir waren von der Zusammenarbeit begeistert. Katrin hat sich von Anfang an intensiv mit dem Inhalt auseinandergesetzt und uns schon beim ersten kreativen Vorschlag überzeugt. Die Detailarbeit bis zum finalen Entwurf lief professionell und zügig. So arbeiten wir am liebsten. Professionell, sympathisch, klar und zuverlässig. Wir gebe eine ganz klare Empfehlung.
Zielgruppe
Firma/Organisation: fornexa - Personal- und Unternehmensberatung
Wir sind eine (zweiköpfige) Personal- und Unternehmensberatung aus der Hamburger Hafencity, die Coachings, Trainings und moderierte Workshops für Fach- und Führungskräfte anbietet.
Zielgruppe:
• Mittelstandsunternehmen
• Geschäftsführer
• Fach- und Führungskräfte
Aufgabenstellung
Ziel des Flyers:
• Kompetenz in den Bereichen Training, Workshop und Coaching vermitteln
• Flyer soll auf Fachmessen eingesetzt werden (Kaltakquise)
• Gesprächsanlässe für den Erstkontakt mit fornexa
Kernbotschaften:
• Weiterentwicklung von Fach- und Führungskräften in Richtung Wirksamkeit
• Zwei Säulen: Haltung und Führungshandwerk
• Firmenindividuelle Konzeption, praxisnah, relevant, abwechslungsreich
• Wertschätzender Umgang, Fokus auf Teilnehmer-Schwerpunkte
Tonalität:
• Professionell + sympathisch + praktisch/pragmatisch/natürlich
Gestaltung:
• Schwerpunkt auf grafische Elemente
• Wenig Text
• Integration von Logo und Grundfarben von fornexa
• Unkonventionelle Gestaltung, Abgrenzung von der Konkurrenz
Themenbeispiele:
• Umgang mit Verschiedenheit
• Konfliktfähigkeit
• Prozessentwicklung/-optimierung
• Führungshandwerk
• Mitarbeiterführung
• Coaching
• Selbstmanagement
• Zeitmanagement
• Schlagfertigkeit
• Unternehmenskultur
Format:
• DIN A4, 1-fach-Faltung, Endformat DIN A5 (Alternativen möglich)
Bildmaterial:
• Aktuell noch nicht vorhanden, Erstellung nach Vorgaben der Designer
Hinweis:
Dieses Briefing ist eine Kurzfassung. Gerne beantworten wir weitergehende Fragen.

```html
<!DOCTYPE html>
<html lang="de">
<head>
<meta charset="utf-8">
<title>fornexa – Flyer Workshops, Trainings & Coachings</title>
<link href="https://fonts.googleapis.com/css2?family=Encode+Sans+Expanded:wght@300;400&family=Open+Sans:ital,wght@0,400;0,600;0,700;1,400;1,600&display=swap" rel="stylesheet">
<style>
:root{
  --green:#95c11f;
  --green-dark:#7fa81a;
  --grey:#6d7278;
  --grey-dark:#5a6066;
  --text:#4a4f55;
  --paper:#ffffff;
  --paper-soft:#f2f2f2;
  --stage:#e3e3e6;
  --sky-top:#d7dde2;
  --sky-mid:#b9c3ca;
  --water:#8e9aa1;
}
*{box-sizing:border-box;margin:0;padding:0}
html,body{width:1200px;height:2520px;overflow:hidden}
body{background:var(--stage);font-family:"Open Sans",sans-serif;color:var(--text)}
.stage{width:1200px;height:840px;position:relative}
.page{position:absolute;top:52px;width:520px;height:735px;background:var(--paper);overflow:hidden;box-shadow:0 14px 30px rgba(0,0,0,.12)}
.single{left:340px}
.spread-left{left:80px}
.spread-right{left:600px}
.spread-left::after{content:"";position:absolute;right:0;top:0;width:18px;height:100%;background:linear-gradient(90deg,transparent,rgba(0,0,0,.06))}

/* cover */
.cover-top{position:absolute;left:0;top:0;width:100%;height:220px;background:var(--paper)}
.brand{position:absolute;left:250px;top:78px;font-family:"Encode Sans Expanded",sans-serif;font-weight:400;font-size:42px;color:var(--green);letter-spacing:.5px}
.tagline{position:absolute;left:252px;top:134px;font-size:12.5px;line-height:1.35;color:var(--grey)}
.cover-photo{position:absolute;left:0;top:220px;width:100%;height:515px;background:linear-gradient(180deg,var(--sky-top) 0%,var(--sky-mid) 48%,var(--water) 62%,#7f8a91 100%)}
.target-badge{position:absolute;left:18px;top:168px;width:104px;height:104px}
.cover-lead{position:absolute;left:40px;top:440px;color:#fff;font-size:17px;line-height:1.35}
.cover-title{position:absolute;left:40px;top:500px;color:#fff;font-family:"Encode Sans Expanded",sans-serif;font-weight:300;font-size:42px;line-height:1.22}

/* inside left */
.why-title{position:absolute;left:50px;top:58px;font-family:"Encode Sans Expanded",sans-serif;font-weight:300;font-size:32px;color:var(--green)}
.reasons{position:absolute;left:50px;top:130px;width:420px;list-style:none}
.reason{display:flex;gap:12px;padding:14px 0;border-bottom:1px solid #dcdcdc}
.reason svg{flex:none;margin-top:3px}
.reason h3{font-size:13px;font-weight:700;color:var(--text)}
.reason p{font-size:11.5px;line-height:1.45;color:var(--grey)}
.office-photo{position:absolute;left:0;top:420px;width:100%;height:315px;background:linear-gradient(160deg,#a7b0b6 0%,#c9cfd3 55%,#dfe2e4 100%)}

/* inside right */
.topics{position:absolute;left:0;top:40px;width:100%;height:380px;background:var(--green);color:#fff;padding:30px 30px 0}
.topics-title{font-family:"Encode Sans Expanded",sans-serif;font-weight:300;font-size:28px;margin-bottom:14px}
.topic-group{border-bottom:1px solid rgba(255,255,255,.55);padding:8px 0 12px}
.topic-group:last-child{border-bottom:none}
.topic-label{font-size:10.5px;font-weight:700;letter-spacing:2.5px;margin-bottom:8px}
.topic-row{display:grid;grid-template-columns:repeat(4,1fr);gap:6px;text-align:center}
.topic{font-size:9.5px;line-height:1.3}
.topic svg{display:block;margin:0 auto 4px}
.meeting-photo{position:absolute;left:0;top:420px;width:100%;height:315px;background:linear-gradient(180deg,#e7e8e8 0%,#c3c8cb 45%,#8d959b 100%)}

/* back */
.quote-photo{position:absolute;left:0;top:0;width:100%;height:230px;background:linear-gradient(120deg,#8e989f 0%,#a9b1b7 50%,#c2c7ca 100%)}
.quote{position:absolute;left:40px;top:40px;color:#fff}
.quote-mark{font-family:"Open Sans",sans-serif;font-weight:700;font-size:64px;line-height:.8;color:var(--green)}
.quote-text{font-family:"Encode Sans Expanded",sans-serif;font-weight:300;font-size:27px;line-height:1.25;margin-top:6px}
.quote-author{font-size:11px;margin-top:8px;font-style:italic}
.team{position:absolute;left:0;top:230px;width:100%;height:330px;background:var(--paper-soft)}
.member{display:flex;gap:22px;align-items:center;padding:0 36px;height:165px;border-bottom:1px solid #dadada}
.member:last-child{border-bottom:none}
.portrait{flex:none;width:78px;height:78px;border-radius:50%;background:linear-gradient(160deg,#c8ccce,#8f979c);border:3px solid #fff}
.member h3{font-size:12.5px;font-weight:700;font-style:italic;color:var(--green);margin-bottom:3px}
.member p{font-size:11px;line-height:1.45;color:var(--grey)}
.member b{color:var(--text)}
.contact{position:absolute;left:0;top:560px;width:100%;height:175px;background:#e9e9e9}
.address{position:absolute;left:36px;top:36px;font-size:11px;line-height:1.55;color:var(--grey)}
.address strong{color:var(--green);font-weight:700}
.pin-badge{position:absolute;left:236px;top:26px;width:52px;height:52px;border-radius:50%;background:var(--green);display:flex;align-items:center;justify-content:center}
.phone-pill{position:absolute;left:246px;top:104px;width:240px;height:52px;border-radius:26px;background:var(--grey);color:#fff;display:flex;align-items:center;gap:16px;padding:0 22px}
.phone-pill span{font-size:14px;line-height:1.2;display:block}
</style>
</head>
<body>

<section class="stage" aria-label="Titelseite">
  <div class="page single">
    <div class="cover-top"></div>
    <div class="brand">fornexa</div>
    <div class="tagline">Die passenden Menschen<br>finden, entwickeln und halten</div>
    <div class="cover-photo" role="img" aria-label="Foto: Hafenpanorama mit Konzerthaus im Nebel über dem Wasser, überlagert von einer Strichzeichnung zweier Personen"></div>
    <svg class="target-badge" viewBox="0 0 104 104">
      <circle cx="52" cy="52" r="49" fill="none" stroke="var(--green)" stroke-width="3"/>
      <circle cx="52" cy="52" r="37" fill="var(--green)"/>
      <circle cx="52" cy="52" r="12" fill="none" stroke="#fff" stroke-width="2"/>
      <circle cx="52" cy="52" r="2.5" fill="#fff"/>
      <path d="M52 34v10M52 60v10M34 52h10M60 52h10" stroke="#fff" stroke-width="2"/>
    </svg>
    <p class="cover-lead">WIRKSAMES Management<br>unterstützen wir mit individuellen</p>
    <h1 class="cover-title">Workshops,<br>Trainings &amp;<br>Coachings</h1>
  </div>
</section>

<section class="stage" aria-label="Innenseiten">
  <div class="page spread-left">
    <h2 class="why-title">Warum fornexa?</h2>
    <ul class="reasons">
      <li class="reason">
        <svg width="14" height="12" viewBox="0 0 14 12"><path d="M1 6l4 4 8-9" fill="none" stroke="var(--green)" stroke-width="2"/></svg>
        <div><h3>Professionell</h3><p>Entwicklung der Führungskräfte zu mehr Wirksamkeit, Fokus und Zielorientierung</p></div>
      </li>
      <li class="reason">
        <svg width="14" height="12" viewBox="0 0 14 12"><path d="M1 6l4 4 8-9" fill="none" stroke="var(--green)" stroke-width="2"/></svg>
        <div><h3>Pragmatisch</h3><p>Hohes Verständnis für die aktuellen und wichtigen Themen mit konkreten Lösungsansätzen</p></div>
      </li>
      <li class="reason">
        <svg width="14" height="12" viewBox="0 0 14 12"><path d="M1 6l4 4 8-9" fill="none" stroke="var(--green)" stroke-width="2"/></svg>
        <div><h3>Sympathisch</h3><p>Das Feedback unserer Teilnehmer zeigt: Wir nehmen die täglichen Hürden ernst und vermitteln Führungshandwerk gepaart mit einer positiven Haltung und Einstellung. Auf den Austausch untereinander und Spaß miteinander legen wir dabei großen Wert.</p></div>
      </li>
    </ul>
    <div class="office-photo" role="img" aria-label="Foto: helles Büro in Grautönen mit Strichzeichnung einer Person mit Fernglas"></div>
  </div>

  <div class="page spread-right">
    <div class="topics">
      <h2 class="topics-title">Unsere Themenfelder</h2>
      <div class="topic-group">
        <div class="topic-label">WORKSHOPS</div>
        <div class="topic-row">
          <div class="topic"><svg width="20" height="18" viewBox="0 0 20 18" fill="none" stroke="#fff" stroke-width="1.4"><rect x="1" y="4" width="13" height="13"/><path d="M8 11l10-10"/></svg>Prozesse durchdenken und gestalten</div>
          <div class="topic"><svg width="18" height="18" viewBox="0 0 18 18" fill="none" stroke="#fff" stroke-width="1.4"><circle cx="9" cy="9" r="8"/><circle cx="9" cy="9" r="4"/><circle cx="9" cy="9" r="1" fill="#fff"/></svg>Gemeinsame Zielentwicklung</div>
          <div class="topic"><svg width="22" height="18" viewBox="0 0 22 18" fill="none" stroke="#fff" stroke-width="1.4"><circle cx="7" cy="5" r="3"/><circle cx="15" cy="5" r="3"/><path d="M1 17c0-4 3-6 6-6s6 2 6 6M9 17c0-4 3-6 6-6s6 2 6 6"/></svg>Teambuilding</div>
          <div class="topic"><svg width="20" height="18" viewBox="0 0 20 18" fill="none" stroke="#fff" stroke-width="1.4"><path d="M1 17L9 9M9 9H4M9 9v5M19 1l-7 7M12 8h5M12 8V3"/></svg>Konfliktklärung</div>
        </div>
      </div>
      <div class="topic-group">
        <div class="topic-label">TRAININGS</div>
        <div class="topic-row">
          <div class="topic"><svg width="20" height="18" viewBox="0 0 20 18" fill="none" stroke="#fff" stroke-width="1.4"><path d="M10 2c5 0 9 3 9 6.5S15 15 10 15c-1 0-2 0-3-.4L2 17l1.5-4C2 12 1 10 1 8.5 1 5 5 2 10 2z"/></svg>Wirksame Kommunikation</div>
          <div class="topic"><svg width="18" height="18" viewBox="0 0 18 18" fill="none" stroke="#fff" stroke-width="1.4"><path d="M9 1v16M3 3h11l2 2-2 2H3zM15 9H4l-2 2 2 2h11z"/></svg>Umgang mit Verschiedenheit</div>
          <div class="topic"><svg width="22" height="18" viewBox="0 0 22 18" fill="none" stroke="#fff" stroke-width="1.4"><path d="M1 15l6-7 5 4 9-10"/></svg>Empathisch führen: klar, transparent, fokussiert</div>
          <div class="topic"><svg width="18" height="18" viewBox="0 0 18 18" fill="none" stroke="#fff" stroke-width="1.4"><rect x="1" y="2" width="16" height="15"/><path d="M5 9l3 3 5-6"/></svg>Entscheidungen richtig treffen</div>
        </div>
      </div>
      <div class="topic-group">
        <div class="topic-label">COACHINGS</div>
        <div class="topic-row">
          <div class="topic"><svg width="20" height="18" viewBox="0 0 20 18" fill="none" stroke="#fff" stroke-width="1.4"><rect x="5" y="1" width="14" height="11"/><rect x="1" y="6" width="14" height="11"/></svg>Schattencoaching</div>
          <div class="topic"><svg width="18" height="18" viewBox="0 0 18 18" fill="none" stroke="#fff" stroke-width="1.4"><rect x="1" y="3" width="16" height="14"/><path d="M5 1v4M13 1v4M1 8h16"/></svg>Selbstmanagement</div>
          <div class="topic"><svg width="20" height="18" viewBox="0 0 20 18" fill="none" stroke="#fff" stroke-width="1.4"><circle cx="10" cy="3" r="2"/><circle cx="3" cy="15" r="2"/><circle cx="10" cy="15" r="2"/><circle cx="17" cy="15" r="2"/><path d="M10 5v8M3 13V9h14v4"/></svg>Vom Kollegen zum Vorgesetzten</div>
        </div>
      </div>
    </div>
    <div class="meeting-photo" role="img" aria-label="Foto: Team in hellem Besprechungsraum im lebhaften Gespräch am Tisch"></div>
  </div>
</section>

<section class="stage" aria-label="Außenseiten">
  <div class="page spread-left">
    <div class="quote-photo" role="img" aria-label="Foto: Hände, die einen Holzklotz aus einem Stapelturm ziehen"></div>
    <blockquote class="quote">
      <div class="quote-mark">”</div>
      <p class="quote-text">Wer zusieht, sieht<br>mehr, als wer mitspielt.</p>
      <p class="quote-author">Wilhelm Brandt</p>
    </blockquote>
    <div class="team">
      <div class="member">
        <div class="portrait" role="img" aria-label="Porträtfoto Jonas Brenner"></div>
        <div>
          <h3>Jonas Brenner</h3>
          <p>langjährige Führungserfahrung in der Lebensmittelindustrie<br>(Konzern und Mittelstand)<br><b>Schwerpunkte:</b> Business Development, Prozessoptimierung,<br>Projektmanagement und Kommunikation</p>
        </div>
      </div>
      <div class="member">
        <div class="portrait" role="img" aria-label="Porträtfoto Lukas Hartwig"></div>
        <div>
          <h3>Lukas Hartwig</h3>
          <p>langjährige Führungserfahrung in Marketing- und Vertrieb bei<br>nationalen und internationalen Markenartikeln<br><b>Schwerpunkte:</b> Führung, Teamentwicklung, Konfliktklärung<br>und Kommunikation</p>
        </div>
      </div>
    </div>
    <div class="contact">
      <address class="address" style="font-style:normal">
        <strong>fornexa oHG</strong><br>
        Am Speicherufer 12 &nbsp;|&nbsp; 20450 Nordhafen<br>
        info@fornexa.com<br>
        www.fornexa.com
      </address>
      <div class="pin-badge">
        <svg width="20" height="24" viewBox="0 0 20 24" fill="none" stroke="#fff" stroke-width="1.8"><path d="M10 23s8-8 8-13.5A8 8 0 0 0 2 9.5C2 15 10 23 10 23z"/><circle cx="10" cy="9.5" r="3"/></svg>
      </div>
      <div class="phone-pill">
        <svg width="22" height="22" viewBox="0 0 24 24" fill="none" stroke="#fff" stroke-width="1.6"><path d="M5 2h4l2 5-3 2a12 12 0 0 0 7 7l2-3 5 2v4a2 2 0 0 1-2 2A19 19 0 0 1 3 4a2 2 0 0 1 2-2z"/></svg>
        <div><span>040-555012-101</span><span>040-555012-102</span></div>
      </div>
    </div>
  </div>

  <div class="page spread-right">
    <div class="cover-top"></div>
    <div class="brand">fornexa</div>
    <div class="tagline">Die passenden Menschen<br>finden, entwickeln und halten</div>
    <div class="cover-photo" role="img" aria-label="Foto: Hafenpanorama mit Konzerthaus im Nebel über dem Wasser, überlagert von einer Strichzeichnung zweier Personen"></div>
    <svg class="target-badge" viewBox="0 0 104 104">
      <circle cx="52" cy="52" r="49" fill="none" stroke="var(--green)" stroke-width="3"/>
      <circle cx="52" cy="52" r="37" fill="var(--green)"/>
      <circle cx="52" cy="52" r="12" fill="none" stroke="#fff" stroke-width="2"/>
      <circle cx="52" cy="52" r="2.5" fill="#fff"/>
      <path d="M52 34v10M52 60v10M34 52h10M60 52h10" stroke="#fff" stroke-width="2"/>
    </svg>
    <p class="cover-lead">WIRKSAMES Management<br>unterstützen wir mit individuellen</p>
    <h2 class="cover-title">Workshops,<br>Trainings &amp;<br>Coachings</h2>
  </div>
</section>

</body>
</html>
```